Business Card Design - Cryotherapy

We need a custom created business card for our company FrostLume Spa. We provide whole body cryotherapy and localized cryotherapy to our clients. Please be creative.
Please see our website for idea's on design.
www.frostlumespa.com
Industry/Entity Type
Business
Contact Information for Business Card
Name, Position, Phone Number, Address, Website, Email
Look and feel
Each slider illustrates characteristics of the customer's brand and the style your logo design should communicate.

```html
<!DOCTYPE html>
<html lang="en">
<head>
<meta charset="utf-8">
<title>FrostLume Spa – Business Card</title>
<link href="https://fonts.googleapis.com/css2?family=Montserrat:wght@400;600&display=swap" rel="stylesheet">
<style>
  :root {
    --canvas: #d9d9d6;
    --card-light: #f3f1e4;
    --card-dark: #2f2c2a;
    --teal: #1b9aa6;
    --green: #1a8a4a;
    --text: #4a4a48;
  }
  html, body {
    margin: 0;
    width: 1200px;
    height: 786px;
    overflow: hidden;
    background: var(--canvas);
    font-family: "Montserrat", sans-serif;
  }
  .stage {
    width: 1200px;
    height: 786px;
    display: flex;
    align-items: center;
    justify-content: center;
    gap: 60px;
  }
  .card {
    position: relative;
    width: 520px;
    height: 297px;
    border-radius: 16px;
    overflow: hidden;
    box-shadow: 0 6px 18px rgba(0,0,0,0.18);
  }
  .card--front { background: var(--card-light); }
  .card--back {
    background: var(--card-dark);
    display: flex;
    align-items: center;
    justify-content: center;
  }
  .card__waves {
    position: absolute;
    left: 0; top: 0;
    width: 520px; height: 297px;
  }
  .brand {
    display: flex;
    align-items: center;
    gap: 10px;
    color: var(--teal);
    font-weight: 600;
    letter-spacing: 0.04em;
  }
  .brand__dot {
    border-radius: 50%;
    background: var(--teal);
  }
  .card--front .brand {
    position: absolute;
    left: 42px; top: 62px;
    font-size: 22px;
  }
  .card--front .brand__dot { width: 34px; height: 34px; }
  .card--back .brand { font-size: 34px; }
  .card--back .brand__dot { width: 52px; height: 52px; }
  .contact {
    position: absolute;
    left: 268px; top: 118px;
    color: var(--text);
    font-size: 12px;
    line-height: 1.55;
  }
  .contact__name {
    margin: 0;
    color: var(--teal);
    font-weight: 600;
    font-size: 15px;
    letter-spacing: 0.06em;
    text-transform: uppercase;
  }
  .contact__role { margin: 0 0 8px; font-size: 12px; }
  .contact__line {
    display: flex;
    align-items: center;
    gap: 8px;
    margin: 0;
  }
  .contact__icon {
    width: 11px; height: 11px;
    border-radius: 2px;
    background: var(--teal);
    flex: none;
  }
  .contact__address { margin: 8px 0 0; }
</style>
</head>
<body>
<main class="stage">
  <section class="card card--front" aria-label="Business card front">
    <svg class="card__waves" viewBox="0 0 520 297" aria-hidden="true">
      <path d="M0 190 C 80 200, 170 230, 230 297 L 0 297 Z" fill="var(--teal)"/>
      <path d="M0 200 C 80 212, 160 240, 214 297 L 0 297 Z" fill="var(--card-light)"/>
      <path d="M0 222 C 70 226, 150 252, 196 297 L 0 297 Z" fill="var(--green)"/>
    </svg>
    <div class="brand"><span class="brand__dot"></span>FrostLume Spa</div>
    <div class="contact">
      <p class="contact__name">Jordan Ellery</p>
      <p class="contact__role">General Manager</p>
      <p class="contact__line"><span class="contact__icon"></span>(555) 014-2231</p>
      <p class="contact__line"><span class="contact__icon"></span>(555) 014-2298</p>
      <p class="contact__line"><span class="contact__icon"></span>info@frostlumespa.com</p>
      <p class="contact__line"><span class="contact__icon"></span>www.frostlumespa.com</p>
      <p class="contact__address">2210 Lakeview Road<br>Suite 40, Maple Grove, IL 60099</p>
    </div>
  </section>
  <section class="card card--back" aria-label="Business card back">
    <div class="brand"><span class="brand__dot"></span>FrostLume Spa</div>
  </section>
</main>
</body>
</html>
```